Rise As Captain Book Cover Design

Book Cover Design Brief
Book Title
Rise As Captain
Subtitle
The 12 Quiet Pillars of Remarkable Command
Author
Orwen Talbrisk
Overview
This book is about leadership that starts within.
Most leadership books focus on tactics or management strategies. This book focuses on the inner disciplines that create powerful leaders — mindset, integrity, focus, empathy, professionalism, honesty, and self-respect.
The tone of the book is bold, direct, confident, and transformational.
This is not a soft or corporate leadership book. It is a call to step up and become the leader you are capable of becoming.
The cover should feel:
• Powerful
• Professional
• Transformational
• Premium
• Memorable
Think best-selling leadership book, not a generic business book.
Target Audience
Business owners
Managers
Entrepreneurs
Team leaders
Professionals who want to grow as leaders
Most readers are ambitious professionals who want to level up their leadership and life.
Design Direction
The design should communicate:
Strength. Discipline. Leadership. Personal transformation.
Avoid cliché leadership visuals like:
• Handshakes
• Office buildings
• Corporate stock imagery
• Teams sitting around tables
The design should feel iconic, bold, and timeless.
Think about covers of successful leadership books such as:
Tiny Rituals
Total Custody
Won't Bend Now
Begin From Core
The 52 Codes of Sway
These covers are simple, powerful, and recognizable even at small sizes.
Typography
The title RISE AS CAPTAIN should be:
• Bold
• Strong
• Dominant on the cover
• Easy to read even at small sizes (important for Quillora thumbnails)
The subtitle should be clean and secondary to the title.
The overall typography should feel strong, modern, and premium.
Color Direction
Designers are free to explore colors, but the cover should feel strong and premium, not playful.
Colors that often work well for leadership books include:
Black
Gold
White
Deep blue
Dark red
High contrast and clarity are important.
Style
Preferred style:
• Clean
• Modern
• Minimal
• Strong contrast
Avoid clutter and overly busy designs.
The goal is to create a cover that feels powerful and professional at first glance.
Deliverables
Front cover design for a leadership book.
Final files should include:
• High resolution artwork
• Editable source files
• Print-ready version suitable for publishing
Goal of the Cover
When someone sees this book on Quillora or in a bookstore, they should immediately think:
“This looks like a serious leadership book.”
The design should feel like it belongs next to books by authors such as:
Marcus Dovell
Brant Feltham
Owen Marsh
Peter Halvorn
A strong, confident cover that attracts leaders who want to grow and perform at a higher level.
Updates
Target Market(s)
Business Owners and High level managers
Look and feel

```html
<!DOCTYPE html>
<html lang="en">
<head>
<meta charset="utf-8">
<title>Rise As Captain — Orwen Talbrisk</title>
<link rel="stylesheet" href="https://fonts.googleapis.com/css2?family=Open+Sans:wght@600;700;800&display=swap">
<style>
  :root {
    --cover-black: #000000;
    --ink-white: #ffffff;
  }
  html, body {
    margin: 0;
    padding: 0;
    width: 927px;
    height: 1200px;
    overflow: hidden;
    background: var(--cover-black);
  }
  .book-cover {
    display: block;
    width: 927px;
    height: 1200px;
    background: var(--cover-black);
  }
  .frame-line {
    fill: none;
    stroke: var(--ink-white);
    stroke-width: 2;
  }
  .author-name {
    font-family: "Open Sans", sans-serif;
    font-weight: 700;
    fill: var(--ink-white);
  }
  .title-word {
    font-family: "Open Sans", sans-serif;
    font-weight: 800;
    fill: var(--ink-white);
  }
  .subtitle {
    font-family: "Open Sans", sans-serif;
    font-weight: 700;
    font-size: 29px;
    fill: var(--ink-white);
  }
</style>
</head>
<body>
<svg class="book-cover" viewBox="0 0 927 1200" xmlns="http://www.w3.org/2000/svg">
  <title>Rise As Captain by Orwen Talbrisk</title>

  <g class="frame">
    <polyline class="frame-line frame-left" points="100,57 19,57 19,1133 100,1133"/>
    <polyline class="frame-line frame-right" points="826,57 907,57 907,1133 826,1133"/>
  </g>

  <text class="author-name" x="126" y="86" textLength="684" lengthAdjust="spacing">
    <tspan font-size="78">O</tspan><tspan font-size="48">RWEN</tspan>
    <tspan font-size="78">T</tspan><tspan font-size="48">ALBRISK</tspan>
  </text>

  <g class="title">
    <text class="title-word title-rise" x="125" y="634" font-size="727" textLength="692" lengthAdjust="spacingAndGlyphs">RISE</text>
    <text class="title-word title-as" x="127" y="958" font-size="446" textLength="672" lengthAdjust="spacingAndGlyphs">AS</text>
    <text class="title-word title-captain" x="188" y="1110" font-size="200" textLength="606" lengthAdjust="spacingAndGlyphs">CAPTAIN</text>
  </g>

  <text class="subtitle" x="120" y="1144" textLength="690" lengthAdjust="spacingAndGlyphs">The 12 Quiet Pillars of Remarkable Command</text>
</svg>
</body>
</html>
```